Business Cards for an 'affordable luxury' inner city home builder in Calgary.

We need a business card design that emulates the progressive, innovative, culture of our company and the modern style of our homes. Use our website www.velmarbuilds-ex.com as a reference for the product we build.

Our company builds homes in the inner city space of Calgary, Alberta. We build affordable luxury.

Target Market(s)

Young professional Families

Contact Information for Business Card

Try to maintain consistency with the logo font and the card font.

Requirements
Must have
• The details must include: Name, education, title, phone number, website and email (Address is not as important)
• The design must be uniques (like our logo), elegant, sophisticated and modern.

```html
<!DOCTYPE html>
<html lang="en">
<head>
<meta charset="utf-8">
<title>Velmar Builds Ltd — Business Card</title>
<link rel="stylesheet" href="https://fonts.googleapis.com/css2?family=Open+Sans:wght@400;700&display=swap">
<style>
  :root {
    --page-bg: #ffffff;
    --card-bg: #000000;
    --text-main: #ffffff;
    --text-soft: #c8c8c8;
    --mark-grey: #8a8a8a;
  }
  html, body {
    margin: 0;
    padding: 0;
    width: 1200px;
    height: 1000px;
    overflow: hidden;
    background: var(--page-bg);
    font-family: "Open Sans", Verdana, sans-serif;
  }
  .canvas {
    position: relative;
    width: 1200px;
    height: 1000px;
  }
  .card {
    position: absolute;
    top: 135px;
    width: 408px;
    height: 736px;
    background: var(--card-bg);
    color: var(--text-main);
  }
  .card--front { left: 162px; }
  .card--back  { left: 646px; }

  .brand {
    position: absolute;
    left: 48px;
    top: 622px;
    display: flex;
    align-items: center;
    gap: 24px;
  }
  .brand__square {
    width: 66px;
    height: 66px;
    background: var(--mark-grey);
  }
  .brand__name {
    margin: 0;
    font-size: 22px;
    font-weight: 700;
    line-height: 24px;
    letter-spacing: 2px;
    text-transform: uppercase;
    color: var(--text-main);
  }

  .person {
    position: absolute;
    left: 47px;
    top: 48px;
  }
  .person__name {
    margin: 0;
    font-size: 24px;
    font-weight: 700;
    line-height: 30px;
  }
  .person__detail {
    margin: 0 0 0 2px;
    font-size: 16px;
    line-height: 20px;
  }
  .contact {
    position: absolute;
    left: 47px;
    top: 146px;
    margin: 0;
    padding: 0;
    list-style: none;
    font-size: 16px;
    line-height: 25px;
    color: var(--text-soft);
  }
  .back-brand {
    position: absolute;
    right: 48px;
    bottom: 44px;
    margin: 0;
    font-size: 14px;
    font-weight: 700;
    letter-spacing: 2px;
    color: var(--mark-grey);
  }
</style>
</head>
<body>
  <main class="canvas">
    <section class="card card--front" aria-label="Card front">
      <div class="brand">
        <div class="brand__square"></div>
        <p class="brand__name">Velmar<br>Builds<br>Ltd</p>
      </div>
    </section>

    <section class="card card--back" aria-label="Card back">
      <div class="person">
        <p class="person__name">Name</p>
        <p class="person__detail">education</p>
        <p class="person__detail">title</p>
      </div>
      <ul class="contact">
        <li>www.velmarbuilds-ex.com</li>
        <li>&nbsp;403-555-0148</li>
        <li>projects@velmarbuilds-ex.com</li>
      </ul>
      <p class="back-brand">VELMAR</p>
    </section>
  </main>
</body>
</html>
```